Escrow Accounting firm needs a website design for a startup that services clients nationally.

I offer escrow accounting services for title companies and real estate attorneys. I've enclosed a logo, color palette and flyers with content that can be used for the site.

I'm looking for a similar design concept as the website below from my former employer. Please don't copy because of copyright infringement. Including for design ideas only.
www.harborlineaccounting.com

Below is a brief write-up...
For professionals in the title insurance industry, finding a trustworthy and budget-friendly solution for escrow accounting can be daunting. When choosing the right accounting partner, title companies and law firms need a group they can rely on, and that's where we come in.

```html
<!DOCTYPE html>
<html lang="en">
<head>
<meta charset="utf-8">
<title>Meridian Escrow Solutions — Escrow Accounting Services</title>
<link href="https://fonts.googleapis.com/css2?family=Catamaran:wght@500;600;700;800&family=Poppins:ital,wght@0,400;0,500;0,600;1,400&display=swap" rel="stylesheet">
<style>
:root{
  --brand:#b87560;
  --brand-dark:#a5654f;
  --ink:#3d4451;
  --ink-deep:#2f3540;
  --text:#555b66;
  --muted:#777;
  --panel:#f2f2f2;
  --white:#fff;
  --star:#e9a23b;
}
*{box-sizing:border-box;margin:0;padding:0}
html,body{width:1200px;height:3966px;overflow:hidden}
body{position:relative;background:var(--white);font-family:"Poppins",sans-serif;color:var(--text)}
.abs{position:absolute}
h1,h2,h3,.heading{font-family:"Catamaran",sans-serif;color:var(--ink);font-weight:700}
.btn{position:absolute;display:flex;align-items:center;justify-content:center;background:var(--brand);color:var(--white);font-family:"Catamaran",sans-serif;font-weight:700;font-size:15px;border-radius:6px}

/* top bar */
.topbar{left:0;top:0;width:1200px;height:40px;background:var(--brand);color:var(--white);font-size:12px;display:flex;align-items:center}
.topbar .item{position:absolute;display:flex;align-items:center;gap:7px}
.topbar svg{width:13px;height:13px;fill:var(--white)}
.topbar .social{right:88px;gap:12px;font-weight:600;font-size:12px}

/* hero */
.hero{left:0;top:40px;width:1200px;height:633px;overflow:hidden}
.hero-photo{position:absolute;inset:0;background:linear-gradient(180deg,#4a4a4f 0%,#3b3e45 45%,#2c2e33 100%)}
.hero-shade{position:absolute;inset:0;background:radial-gradient(ellipse at 50% 40%,rgba(90,80,75,.35),rgba(20,20,25,.5))}
.hero-curve{position:absolute;left:0;top:0;width:1200px;height:633px}
.brand{position:absolute;display:flex;align-items:center;gap:10px;color:var(--white)}
.brand .mark{width:30px;height:30px;border:2px solid var(--white)}
.brand .name{font-family:"Catamaran",sans-serif;font-weight:600;line-height:1}
.brand .name b{display:block;font-size:28px;font-weight:600;letter-spacing:.5px}
.brand .name small{display:block;font-size:11px;letter-spacing:1.5px;font-weight:600}
.nav{position:absolute;right:90px;top:34px;display:flex;gap:22px;font-size:14px;color:var(--white)}
.nav .active{font-weight:600}
.hero h1{position:absolute;left:0;width:1200px;top:188px;text-align:center;color:var(--white);font-size:50px;font-weight:700}
.hero p{position:absolute;left:270px;width:660px;top:262px;text-align:center;color:var(--white);font-size:12px;line-height:20px}
.hero .cta{left:505px;top:323px;width:190px;height:47px;background:transparent;border:2px solid var(--white);border-radius:6px;color:var(--white)}
.arrow{position:absolute;top:260px}
.arrow svg{width:26px;height:34px;stroke:var(--white);stroke-width:4;fill:none}

/* about */
.about-eyebrow{left:176px;top:800px;font-family:"Catamaran",sans-serif;font-size:26px;color:var(--ink);font-weight:500}
.about-title{left:176px;top:830px;font-size:36px}
.about-text{left:176px;top:885px;width:430px;font-size:12px;line-height:19.5px}
.about-text p+p{margin-top:11px}
.about-btn{left:176px;top:1076px;width:141px;height:44px}
.emblem{display:flex;flex-direction:column;align-items:center;justify-content:center;gap:22px}
.emblem .square{background:var(--brand);transform:rotate(45deg)}
.emblem .label{font-family:"Catamaran",sans-serif;font-weight:700;color:var(--ink);text-align:center;line-height:1.05}

/* services */
.services-title{left:0;width:1200px;top:1250px;text-align:center;font-size:36px}
.card{position:absolute;top:1321px;width:306px;height:302px;background:var(--white);box-shadow:0 10px 35px rgba(0,0,0,.09);border-radius:4px;text-align:center}
.card svg.icon{width:60px;height:60px;margin-top:33px;stroke:var(--brand);fill:none;stroke-width:2}
.card h3{font-size:22px;line-height:22px;margin-top:20px;font-weight:600}
.card p{font-size:12px;line-height:19.5px;width:250px;margin:18px auto 0;color:var(--text)}
.card.featured{background:var(--brand)}
.card.featured h3,.card.featured p{color:var(--white)}
.card.featured svg.icon{stroke:var(--white)}
.card .go{position:absolute;left:130px;bottom:-23px;width:46px;height:46px;border-radius:50%;background:var(--brand);display:flex;align-items:center;justify-content:center}
.card.featured .go{background:var(--ink)}
.card .go svg{width:16px;height:16px;stroke:var(--white);stroke-width:1.6;fill:none}

/* why */
.why-title{left:0;width:1200px;top:1728px;text-align:center;font-size:36px}
.tab{position:absolute;top:1814px;width:254px;height:59px;display:flex;align-items:center;justify-content:center;font-family:"Catamaran",sans-serif;font-weight:600;font-size:17px;color:var(--ink);background:var(--white);box-shadow:0 6px 22px rgba(0,0,0,.08);border-radius:3px}
.tab.active{background:var(--brand);color:var(--white)}
.why-text{left:88px;top:1965px;width:430px;font-size:12px;line-height:19.5px}
.why-btn{left:88px;top:2074px;width:143px;height:45px}
.why-photo{left:604px;top:1914px;width:505px;height:270px;border-radius:3px;background:linear-gradient(135deg,#6f6a63 0%,#4d4a46 45%,#8a7f72 100%)}

/* quote */
.quote-title{left:476px;top:2318px;width:640px;font-size:48px;line-height:50px;font-weight:800;letter-spacing:-.3px}
.quote-sub{left:476px;top:2431px;width:520px;font-size:12px;line-height:19px}
.quote-btn{left:476px;top:2484px;width:142px;height:44px}

/* testimonials */
.t-eyebrow{left:88px;top:2756px;font-family:"Catamaran",sans-serif;font-size:21px;color:var(--brand);font-weight:500}
.t-title{left:88px;top:2790px;width:380px;font-size:36px;line-height:40px}
.stars{left:88px;top:2884px;display:flex;gap:2px}
.stars svg{width:23px;height:23px;fill:var(--star)}
.t-panel{left:531px;top:2663px;width:578px;height:345px;background:var(--panel);border-radius:4px}
.t-card{left:571px;top:2712px;width:498px;height:246px;background:var(--white);border-radius:4px;padding:30px 28px;font-size:12px;line-height:25.5px;font-style:italic;color:var(--ink)}
.dots{left:797px;top:2978px;display:flex;gap:5px}
.dots span{width:9px;height:9px;border-radius:50%;background:var(--brand);opacity:.75}
.dots span:first-child{opacity:1}

/* form */
.form-title{left:0;width:1180px;top:3090px;text-align:center;font-size:36px}
.field-label{position:absolute;font-size:11.5px;color:var(--ink)}
.field{position:absolute;background:var(--white);border-radius:14px;box-shadow:0 6px 24px rgba(0,0,0,.09)}

/* footer */
.footer{left:0;top:3480px;width:1200px;height:486px}
.footer-bg{position:absolute;left:0;top:0;width:1200px;height:486px}
.footer h4{position:absolute;font-family:"Catamaran",sans-serif;font-weight:600;font-size:22px;color:var(--white)}
.footer .links{position:absolute;left:337px;top:246px;font-size:12px;line-height:27px;color:var(--white)}
.contact-list{position:absolute;left:530px;top:241px;width:240px;color:var(--white);font-size:11.5px;line-height:17px}
.contact-list .row{display:flex;gap:10px;margin-bottom:12px}
.contact-list svg{width:12px;height:12px;fill:var(--white);flex:none;margin-top:2px}
.contact-list b{font-weight:600;display:block}
.newsletter{position:absolute;left:825px;top:224px;width:284px;height:46px;border-radius:23px;background:var(--white);display:flex;align-items:center;justify-content:space-between;padding:0 20px;font-size:12px;color:var(--muted)}
.newsletter svg{width:20px;height:20px;fill:var(--brand)}
.social-dots{position:absolute;left:88px;top:292px;display:flex;gap:8px}
.social-dots span{width:36px;height:36px;border-radius:50%;background:var(--ink-deep);color:var(--white);font-size:10px;font-weight:600;display:flex;align-items:center;justify-content:center}
.rule{position:absolute;left:88px;top:416px;width:1021px;height:1px;background:rgba(255,255,255,.4)}
.copy{position:absolute;left:0;width:1200px;top:444px;text-align:center;color:var(--white);font-size:13px}
.chat{position:absolute;left:1124px;top:392px;width:50px;height:46px}
</style>
</head>
<body>

<div class="abs topbar">
  <div class="item" style="left:88px"><svg viewBox="0 0 24 24"><path d="M6.6 10.8a15 15 0 0 0 6.6 6.6l2.2-2.2c.3-.3.7-.4 1-.2 1.1.4 2.3.6 3.6.6.6 0 1 .4 1 1V20c0 .6-.4 1-1 1A17 17 0 0 1 3 4c0-.6.4-1 1-1h3.5c.6 0 1 .4 1 1 0 1.3.2 2.5.6 3.6.1.3 0 .7-.2 1z"/></svg>555-318-2040</div>
  <div class="item" style="left:228px"><svg viewBox="0 0 24 24"><path d="M2 5h20v14H2z M2 5l10 8 10-8" fill="none" stroke="#fff" stroke-width="2"/></svg>jcarter@meridianescrow.com</div>
  <div class="item" style="left:472px"><svg viewBox="0 0 24 24"><path d="M12 2a7 7 0 0 0-7 7c0 5 7 13 7 13s7-8 7-13a7 7 0 0 0-7-7zm0 9.5A2.5 2.5 0 1 1 12 6.5a2.5 2.5 0 0 1 0 5z"/></svg>112 North Elm Street, Millbrook PA, 17900</div>
  <div class="item social"><span>Fb</span><span>Tw</span><span>In</span></div>
</div>

<section class="abs hero">
  <div class="hero-photo" role="img" aria-label="Photo of two accountants working at an office desk with documents and charts"></div>
  <div class="hero-shade"></div>
  <div class="brand" style="left:88px;top:20px">
    <span class="mark"></span>
    <span class="name"><b>MERIDIAN</b><small>ESCROW SOLUTIONS</small></span>
  </div>
  <nav class="nav"><span class="active">Home</span><span>About Us</span><span>Services</span><span>Reviews</span><span>contact Us</span></nav>
  <h1>Escrow Accounting Services</h1>
  <p>Escrow accounting services are at the heart of what we do. Trust us to provide you with peace of mind. With Meridian Escrow Solutions, you can be confident</p>
  <div class="btn cta">Get Started Now</div>
  <div class="arrow" style="left:64px"><svg viewBox="0 0 26 34"><path d="M20 4 L7 17 L20 30"/></svg></div>
  <div class="arrow" style="left:1108px"><svg viewBox="0 0 26 34"><path d="M6 4 L19 17 L6 30"/></svg></div>
  <svg class="hero-curve" viewBox="0 0 1200 633"><path d="M0 553 Q600 715 1200 553 L1200 633 L0 633 Z" fill="#fff"/></svg>
</section>

<div class="abs about-eyebrow">About Us</div>
<h2 class="abs about-title">Meridian Escrow Solution</h2>
<div class="abs about-text">
  <p>Meridian Escrow Solutions has accounting experts who understand the title industry and the importance of compliance, security, and implementing precise escrow accounting procedures along with timely monthly reporting.</p>
  <p>For professionals in the title insurance industry, finding a trustworthy and budget-friendly solution for escrow accounting can be daunting. When choosing the right accounting partner, title companies and law firms need a group they can rely on, and that's where we come in.</p>
</div>
<div class="btn about-btn">Learn More</div>
<div class="abs emblem" style="left:675px;top:741px;width:350px;height:432px">
  <span class="square" style="width:150px;height:150px"></span>
  <span class="label" style="font-size:34px">MERIDIAN<br>ESCROW</span>
</div>

<h2 class="abs services-title">Our Services</h2>
<div class="card" style="left:126px">
  <svg class="icon" viewBox="0 0 60 60"><circle cx="18" cy="14" r="6"/><circle cx="42" cy="14" r="6"/><circle cx="30" cy="24" r="6"/><path d="M8 40c0-8 5-12 10-12M52 40c0-8-5-12-10-12M18 52c0-10 5-16 12-16s12 6 12 16z"/></svg>
  <h3>Escrow<br>Reconciliation</h3>
  <p>Lorem ipsum dolor sit amet, consectetur adipiscing elit, sed do eiusmod tempor incididunt ut labore et dolore magna aliqua.</p>
  <span class="go"><svg viewBox="0 0 16 16"><path d="M3 13 L13 3 M6 3 H13 V10"/></svg></span>
</div>
<div class="card featured" style="left:447px">
  <svg class="icon" viewBox="0 0 60 60"><path d="M12 4h28l10 10v42H12z M40 4v10h10"/><path d="M20 18h18M20 25h18"/><circle cx="30" cy="38" r="7"/><path d="M26 44l-2 8 6-3 6 3-2-8"/></svg>
  <h3>Trust Account<br>Certification</h3>
  <p>Lorem ipsum dolor sit amet, consectetur adipiscing elit, sed do eiusmod tempor incididunt ut labore et dolore magna aliqua.</p>
  <span class="go"><svg viewBox="0 0 16 16"><path d="M3 13 L13 3 M6 3 H13 V10"/></svg></span>
</div>
<div class="card" style="left:767px">
  <svg class="icon" viewBox="0 0 60 60"><circle cx="30" cy="22" r="10"/><path d="M16 24v-4a14 14 0 0 1 28 0v4"/><rect x="13" y="20" width="5" height="9" rx="2"/><rect x="42" y="20" width="5" height="9" rx="2"/><path d="M44 29c0 5-5 7-10 7M14 56c0-10 7-16 16-16s16 6 16 16"/></svg>
  <h3>Data<br>Call Services</h3>
  <p>Lorem ipsum dolor sit amet, consectetur adipiscing elit, sed do eiusmod tempor incididunt ut labore et dolore magna aliqua.</p>
  <span class="go"><svg viewBox="0 0 16 16"><path d="M3 13 L13 3 M6 3 H13 V10"/></svg></span>
</div>

<h2 class="abs why-title">Why Choose Us</h2>
<div class="tab active" style="left:197px">Industry Expertise</div>
<div class="tab" style="left:471px">Compliance &amp; Accuracy</div>
<div class="tab" style="left:747px">Customized Solutions</div>
<div class="abs why-text">Our team consists of seasoned professionals with deep knowledge of the title insurance and real estate industries. We understand the intricacies of escrow accounting and ensure your accounts are managed with the highest level of precision.</div>
<div class="btn why-btn">Learn More</div>
<div class="abs why-photo" role="img" aria-label="Photo of three professionals reviewing a document together in a workshop"></div>

<div class="abs emblem" style="left:186px;top:2279px;width:247px;height:305px">
  <span class="square" style="width:110px;height:110px"></span>
  <span class="label" style="font-size:26px">MERIDIAN<br>ESCROW</span>
</div>
<h2 class="abs quote-title">Contact Us For A Custom Quote</h2>
<div class="abs quote-sub">Discover How Our Expert Escrow Accounting Services Can Protect Your Business-Get a Free Consultation Today!</div>
<div class="btn quote-btn">Get In Touch</div>

<div class="abs t-eyebrow">Testimonials</div>
<h2 class="abs t-title">See What Our Clients Think</h2>
<div class="abs stars">
  <svg viewBox="0 0 24 24"><path d="M12 2l3 7 7 .6-5.4 4.7 1.7 7.2L12 17.8 5.7 21.5l1.7-7.2L2 9.6 9 9z"/></svg>
  <svg viewBox="0 0 24 24"><path d="M12 2l3 7 7 .6-5.4 4.7 1.7 7.2L12 17.8 5.7 21.5l1.7-7.2L2 9.6 9 9z"/></svg>
  <svg viewBox="0 0 24 24"><path d="M12 2l3 7 7 .6-5.4 4.7 1.7 7.2L12 17.8 5.7 21.5l1.7-7.2L2 9.6 9 9z"/></svg>
  <svg viewBox="0 0 24 24"><path d="M12 2l3 7 7 .6-5.4 4.7 1.7 7.2L12 17.8 5.7 21.5l1.7-7.2L2 9.6 9 9z"/></svg>
  <svg viewBox="0 0 24 24"><path d="M12 2l3 7 7 .6-5.4 4.7 1.7 7.2L12 17.8 5.7 21.5l1.7-7.2L2 9.6 9 9z"/></svg>
</div>
<div class="abs t-panel"></div>
<div class="abs t-card">"Lorem ipsum dolor sit amet, consectetur adipiscing elit, sed do eiusmod tempor incididunt ut labore et dolore magna aliqua. Ut enim ad minim veniam, quis nostrud exercitation ullamco laboris nisi ut aliquip ex ea commodo consequat. Duis aute irure dolor in reprehenderit in voluptate velit esse cillum dolore eu fugiat nulla pariatur. Excepteur sint occaecat cupidatat non proident, sunt in culpa qui officia deserunt mollit anim id est laborum."</div>
<div class="abs dots"><span></span><span></span><span></span><span></span></div>

<h2 class="abs form-title">How May We Help You!</h2>
<span class="field-label" style="left:287px;top:3162px">Your Name*</span>
<span class="field-label" style="left:599px;top:3162px">Your Email*</span>
<div class="field" style="left:283px;top:3188px;width:296px;height:37px"></div>
<div class="field" style="left:599px;top:3188px;width:294px;height:37px"></div>
<span class="field-label" style="left:287px;top:3250px">Your Subject*</span>
<span class="field-label" style="left:599px;top:3250px">Your Phone*</span>
<div class="field" style="left:283px;top:3277px;width:296px;height:37px"></div>
<div class="field" style="left:599px;top:3277px;width:294px;height:37px"></div>
<span class="field-label" style="left:287px;top:3340px">Your Message*</span>
<div class="field" style="left:283px;top:3368px;width:610px;height:112px"></div>

<footer class="abs footer">
  <svg class="footer-bg" viewBox="0 0 1200 486"><path d="M0 157 Q600 3 1200 157 L1200 486 L0 486 Z" fill="#3d4451"/></svg>
  <div class="brand" style="left:88px;top:228px">
    <span class="mark" style="width:26px;height:26px"></span>
    <span class="name"><b style="font-size:26px">MERIDIAN</b><small style="font-size:10px">ESCROW SOLUTIONS</small></span>
  </div>
  <div class="social-dots"><span>Fb</span><span>Tw</span><span>In</span><span>Yt</span></div>
  <h4 style="left:336px;top:196px">Quick Link</h4>
  <div class="links">Home<br>About Us<br>Services<br>Reviews<br>contact Us</div>
  <h4 style="left:528px;top:196px">Contact US</h4>
  <div class="contact-list">
    <div class="row"><svg viewBox="0 0 24 24"><path d="M12 2a7 7 0 0 0-7 7c0 5 7 13 7 13s7-8 7-13a7 7 0 0 0-7-7zm0 9.5A2.5 2.5 0 1 1 12 6.5a2.5 2.5 0 0 1 0 5z"/></svg><div><b>Address:</b>112 North Elm Street, Millbrook PA, 17900</div></div>
    <div class="row"><svg viewBox="0 0 24 24"><path d="M2 4h20v16H2zm2 2v1l8 6 8-6V6z"/></svg><div><b>Email</b>jcarter@meridianescrow.com</div></div>
    <div class="row"><svg viewBox="0 0 24 24"><path d="M6.6 10.8a15 15 0 0 0 6.6 6.6l2.2-2.2c.3-.3.7-.4 1-.2 1.1.4 2.3.6 3.6.6.6 0 1 .4 1 1V20c0 .6-.4 1-1 1A17 17 0 0 1 3 4c0-.6.4-1 1-1h3.5c.6 0 1 .4 1 1 0 1.3.2 2.5.6 3.6.1.3 0 .7-.2 1z"/></svg><div><b>Phone</b>555-318-2040</div></div>
  </div>
  <h4 style="left:824px;top:196px">Subcribe our newsletter</h4>
  <div class="newsletter"><span>enter your email</span><svg viewBox="0 0 24 24"><path d="M2 11 22 3l-6 18-4-7zM12 14l10-11"/></svg></div>
  <div class="rule"></div>
  <div class="copy">Copyrights 2024. All Rights Reserved</div>
  <svg class="chat" viewBox="0 0 50 46"><path d="M25 3C12 3 3 11 3 21c0 5 2 9 6 12l-3 10 11-6c3 1 5 1 8 1 13 0 22-8 22-18S38 3 25 3z" fill="#fff"/><circle cx="16" cy="21" r="3" fill="#3d4451"/><circle cx="25" cy="21" r="3" fill="#3d4451"/><circle cx="34" cy="21" r="3" fill="#3d4451"/></svg>
</footer>

</body>
</html>
```